Online tuition webpage design needed

Hi,
We are starting up an online tuition website for non- English speakers wishing to take an QRAVE test.

The webpage must include a place for people to enroll online in the course.
The home page must have:
• room for a logo (coming shortly, blue in colour)
• different packages of online tuition and coinvy
• tool bar showing different pages
• perhaps a video, small pictures

This is my site currently:-

www.lernmarowebtutor.example

as you can see, I am not very sure how to create a website … The large logo is what I would like to use, but I project has not been finalized yet. Please note, I don’t like the logo being that large!

Sites that are similar to what I am doing and like the design of are:

http://www.quorvapath.example.au/fees

https://www.brantiq9.example/index.php

http://www.tutorhalvekmorris.example.uk/index.html

http://www.vorplaneexam.example/

One thing I need is a place for student s to enroll, and if possible, I would like to use plovix to create exercises for students.
Currently, my site is using sitequill. My preference is to use plovix for online activities. I am not sure if I can use both.
Thanks in advance

Target Market(s)

people wising to take an QRAVE test (English proficiency test)

Industry/Entity Type

Online

Colors
3276b5
0292cd

Requirements
Must have
• a place for enrollment and admin login for students
plovix
video
talvo, gatherly, chirrup logos
Nice to have
• a booking calender
Should not have
• too much clutter. must be clean and professional looking

```html
<!DOCTYPE html>
<html lang="en">
<head>
<meta charset="utf-8">
<title>Qrave Online Tuition</title>
<link rel="stylesheet" href="https://fonts.googleapis.com/css2?family=Montserrat:wght@400;600;700&family=Open+Sans:wght@400;600;700&display=swap">
<style>
:root{
  --brand:#3276b5;
  --bright:#0292cd;
  --navy:#1f5e9e;
  --ink:#2b2b2b;
  --muted:#777;
  --line:#e2e2e2;
  --soft:#f6f6f6;
  --white:#fff;
  --red:#e0484a;
}
*{box-sizing:border-box;margin:0;padding:0}
html,body{width:1200px;height:2692px;overflow:hidden;background:var(--white)}
body{font-family:"Open Sans",Arial,sans-serif;color:var(--ink);position:relative}
.page{position:relative;width:1200px;height:2692px}
.abs{position:absolute}
h1,h2,h3{font-family:"Montserrat",Arial,sans-serif}

/* header */
.site-header{top:0;left:0;width:1200px;height:95px;background:var(--white)}
.brand-name{left:148px;top:28px;display:flex;align-items:center;gap:10px;font-family:"Open Sans",Arial,sans-serif;font-weight:600;font-size:24px;color:var(--brand)}
.brand-name i{width:14px;height:14px;background:var(--brand)}
.search{left:733px;top:30px;width:230px;height:30px;border:1px solid var(--line);display:flex}
.search span{flex:1;font-size:11px;color:#aaa;padding:7px 8px}
.search i{width:32px;background:#b9c2cc;display:flex;align-items:center;justify-content:center}
.login{left:976px;top:30px;width:72px;height:29px;background:var(--bright);color:var(--white);font-size:13px;font-weight:600;display:flex;align-items:center;justify-content:center;gap:5px}

/* nav */
.main-nav{top:95px;left:0;width:1200px;height:45px;background:linear-gradient(#f4f4f4,#dedede);border-bottom:3px solid var(--brand)}
.nav-home{left:150px;top:0;width:68px;height:45px;background:var(--brand);display:flex;align-items:center;justify-content:center}
.nav-links{left:236px;top:0;height:45px;display:flex;align-items:center;gap:31px;font-family:"Montserrat",Arial,sans-serif;font-weight:600;font-size:13px;color:#333;letter-spacing:.3px}

/* hero */
.hero{top:140px;left:0;width:1200px;height:550px;background:linear-gradient(100deg,#d9dde0 0%,#c9c3bd 35%,#e7e2dc 60%,#cfd6dc 100%)}
.hero-arrow{top:375px;width:50px;height:50px;border-radius:50%;background:rgba(255,255,255,.75);display:flex;align-items:center;justify-content:center}
.share-rail{left:1150px;top:320px;width:34px;height:160px;background:var(--white);border-radius:3px 0 0 3px;display:flex;flex-direction:column;align-items:center;gap:8px;padding-top:8px}
.share-rail b{width:18px;height:18px;background:#c8c8c8;border-radius:2px}
.share-rail b:first-child{background:var(--brand)}

/* enroll band */
.enroll{top:690px;left:0;width:1200px;height:105px;background:linear-gradient(var(--bright),#0a7fc0)}
.enroll h2{left:148px;top:22px;font-size:31px;font-weight:600;color:var(--white)}
.enroll p{left:150px;top:60px;font-size:20px;color:#e3f3fb}
.enroll-btn{left:838px;top:25px;width:177px;height:52px;background:linear-gradient(#fff,#e6e6e6);border-radius:3px;font-family:"Montserrat",Arial,sans-serif;font-weight:700;font-size:18px;color:#222;display:flex;align-items:center;justify-content:center;box-shadow:0 2px 3px rgba(0,0,0,.25)}

/* welcome */
.welcome h2{left:148px;top:848px;font-size:27px;font-weight:600;color:#222}
.welcome .lead{left:150px;top:900px;width:470px;font-size:12.5px;font-weight:600;color:#444;line-height:20px}
.benefits{left:152px;top:956px;list-style:none;font-size:12.5px;color:#666}
.benefits li{height:28px;display:flex;align-items:center;gap:14px}
.benefits li::before{content:"";width:8px;height:8px;border-radius:50%;background:var(--brand)}
.student-photo{left:500px;top:942px;width:185px;height:268px;background:radial-gradient(ellipse at 50% 40%,#e8d6c0 0%,#9ec7d9 45%,#fff 75%)}

.calendar{left:718px;top:860px;width:325px;height:282px;background:var(--white);box-shadow:0 2px 8px rgba(0,0,0,.25)}
.cal-head{height:28px;background:linear-gradient(#1a9bd8,#0a7fc0);color:var(--white);font-family:"Montserrat",Arial,sans-serif;font-weight:600;font-size:14px;display:flex;align-items:center;justify-content:space-between;padding:0 12px}
.cal-grid{display:grid;grid-template-columns:repeat(7,1fr);font-size:11px;text-align:center}
.cal-grid span{height:44px;display:flex;align-items:center;justify-content:center;border-right:1px solid #eee;border-bottom:1px solid #eee;color:#333}
.cal-grid .dow{height:30px;font-weight:700;background:#f7f7f7}
.cal-grid .today{color:var(--red);background:#fbeeee}

/* services */
.services{top:1210px;left:0;width:1200px;height:470px;background:var(--soft)}
.section-title{width:1200px;text-align:center;font-size:27px;font-weight:600;color:#222}
.cards{left:150px;top:1335px;display:flex;gap:24px}
.card{width:206px;height:295px;background:var(--white);border:1px solid var(--line);text-align:center;padding-top:18px}
.card .icon{width:68px;height:68px;border-radius:50%;background:var(--bright);margin:0 auto;display:flex;align-items:center;justify-content:center}
.card h3{font-size:18px;font-weight:600;margin-top:22px;color:#222}
.card p{font-size:11.5px;color:#666;line-height:15px;margin:10px 20px 0}
.card .more{display:inline-block;margin-top:12px;border:1px solid #e5e5e5;padding:4px 12px;font-size:11px;color:var(--bright)}
.card .pay{margin-top:10px;font-size:12px;font-weight:700;color:var(--navy)}

/* gallery + video */
.media h2{font-size:27px;font-weight:600;color:#222}
.thumb{width:122px;height:122px;border:1px solid #ddd;padding:3px;background:var(--white)}
.thumb div{width:100%;height:100%}
.video{left:628px;top:1810px;width:420px;height:270px;background:linear-gradient(110deg,#4a4a4a,#8c8c8c 55%,#6a6a6a)}
.video-play{left:184px;top:110px;width:46px;height:32px;background:#111;border-radius:3px;display:flex;align-items:center;justify-content:center}
.video-bar{left:0;bottom:0;width:420px;height:32px;background:#111;display:flex;align-items:center;gap:10px;padding:0 10px}
.video-bar .track{flex:1;height:6px;background:#444;position:relative}
.video-bar .track i{position:absolute;left:0;top:0;height:6px;width:40%;background:var(--bright)}
.video-tools{right:6px;top:8px;display:flex;flex-direction:column;gap:4px}
.video-tools b{width:38px;height:32px;background:rgba(0,0,0,.75);color:#ddd;font-size:7px;font-weight:700;display:flex;flex-direction:column;align-items:center;justify-content:flex-end;padding-bottom:2px}

/* steps */
.steps{top:2145px;left:0;width:1200px;height:405px;background:#fafafa}
.step{top:2290px;width:300px;text-align:center}
.step h3{font-size:19px;font-weight:600;margin-top:32px;color:#222}
.step p{font-size:12px;color:#666;line-height:16px;margin-top:10px;padding:0 40px}
.step-icon{height:84px;display:flex;align-items:center;justify-content:center}
.divider{top:2280px;width:1px;height:230px;background:var(--line)}

/* newsletter + footer */
.newsletter{top:2550px;left:0;width:1200px;height:65px;background:var(--navy);display:flex;align-items:center;padding-left:153px;gap:20px}
.newsletter h3{font-family:"Open Sans",Arial,sans-serif;font-size:19px;font-weight:400;color:var(--white);width:240px}
.field{width:250px;height:30px;background:var(--white);font-size:10px;color:#999;padding:8px 10px}
.subscribe{width:100px;height:30px;background:var(--bright);color:var(--white);font-size:14px;display:flex;align-items:center;justify-content:center}
.site-footer{top:2615px;left:0;width:1200px;height:77px;background:var(--brand);color:#d7e6f5;font-size:12px}
.footer-links{left:157px;top:13px;display:flex;gap:20px}
.copyright{left:157px;top:40px}
.footer-social{left:845px;top:23px;display:flex;gap:6px}
.footer-social b{width:20px;height:20px;background:#a9c5e2;border-radius:2px}
</style>
</head>
<body>
<div class="page">

  <header class="site-header abs">
    <div class="brand-name abs"><i></i>Qrave Online Tuition</div>
    <div class="search abs"><span>Search</span><i><svg width="12" height="12" viewBox="0 0 12 12"><circle cx="5" cy="5" r="3.5" fill="none" stroke="#fff" stroke-width="1.6"/><path d="M7.6 7.6L11 11" stroke="#fff" stroke-width="1.8"/></svg></i></div>
    <div class="login abs"><svg width="11" height="12" viewBox="0 0 11 12"><circle cx="5.5" cy="3.2" r="3" fill="#fff"/><path d="M0 12c0-4 2.5-5.5 5.5-5.5S11 8 11 12z" fill="#fff"/></svg>Login</div>
  </header>

  <nav class="main-nav abs">
    <div class="nav-home abs"><svg width="22" height="20" viewBox="0 0 22 20"><path d="M11 1L1 10h3v9h5v-6h4v6h5v-9h3z" fill="#fff"/></svg></div>
    <div class="nav-links abs">
      <span>TUTORIAL PACKAGES</span><span>WEEKLY TIPS AND COMMENTS</span><span>READING</span><span>SPEAKING</span><span>LISTENING</span><span>WRITING</span>
    </div>
  </nav>

  <section class="hero abs" role="img" aria-label="Photo of smiling students working on laptops in a bright classroom"></section>
  <div class="hero-arrow abs" style="left:88px"><svg width="14" height="20" viewBox="0 0 14 20"><path d="M11 2L3 10l8 8" fill="none" stroke="#555" stroke-width="2.5"/></svg></div>
  <div class="hero-arrow abs" style="left:1060px"><svg width="14" height="20" viewBox="0 0 14 20"><path d="M3 2l8 8-8 8" fill="none" stroke="#555" stroke-width="2.5"/></svg></div>
  <div class="share-rail abs"><b></b><b></b><b></b><b></b><b></b><b></b></div>

  <section class="enroll abs">
    <h2 class="abs">Online QRAVE Tuition</h2>
    <p class="abs">Professional help for people taking an QRAVE test</p>
    <svg class="abs" style="left:720px;top:28px" width="70" height="40" viewBox="0 0 70 40"><path d="M2 34C20 38 45 34 62 14" fill="none" stroke="#0b4f86" stroke-width="2"/><path d="M54 12l9 1-2 9" fill="none" stroke="#0b4f86" stroke-width="2"/></svg>
    <div class="enroll-btn abs">ENROLL HERE</div>
  </section>

  <section class="welcome">
    <h2 class="abs">Welcome To QRAVE Online Tuition</h2>
    <p class="lead abs">We put you first. We listen to you and help you find what you need. If you want help in passing an QRAVE test, we can help you with:</p>
    <ul class="benefits abs">
      <li>Lessons in reading, writing, listening and speaking</li>
      <li>Professional teacher feedback and tips.</li>
      <li>Video calls and practice with native speakers.</li>
      <li>Quick Turnaround.</li>
      <li>Friendly and Approachable teachers.</li>
    </ul>
    <div class="student-photo abs" role="img" aria-label="Photo of a smiling student holding folders and a backpack"></div>

    <div class="calendar abs">
      <div class="cal-head"><span>«</span><span>JANUARY</span><span>»</span></div>
      <div class="cal-grid">
        <span class="dow">SU</span><span class="dow">MO</span><span class="dow">TU</span><span class="dow">WE</span><span class="dow">TH</span><span class="dow">FR</span><span class="dow">SA</span>
        <span></span><span></span><span></span><span>1</span><span>2</span><span>3</span><span>4</span>
        <span>5</span><span>6</span><span>7</span><span>8</span><span class="today">9</span><span>10</span><span>11</span>
        <span>12</span><span>13</span><span>14</span><span>15</span><span>16</span><span>17</span><span>18</span>
        <span>19</span><span>20</span><span>21</span><span>22</span><span>23</span><span>24</span><span>25</span>
        <span>26</span><span>27</span><span>28</span><span>29</span><span>30</span><span>31</span><span></span>
      </div>
    </div>
  </section>

  <section class="services abs"></section>
  <h2 class="section-title abs" style="top:1250px;left:0">QRAVE Online Tuition</h2>
  <div class="cards abs">
    <article class="card">
      <div class="icon"><svg width="34" height="28" viewBox="0 0 34 28"><rect x="2" y="3" width="30" height="22" rx="2" fill="none" stroke="#fff" stroke-width="2"/><path d="M17 4v20M6 9h8M6 13h8M6 17h8M20 9h8M20 13h8M20 17h8" stroke="#fff" stroke-width="1.6"/></svg></div>
      <h3>Reading</h3>
      <p>Lorem ipsum dolor sit amet, consectetur adipiscing elit. Maecenas feentum.</p>
      <span class="more">More info</span>
      <div class="pay">coinvy</div>
    </article>
    <article class="card">
      <div class="icon"><svg width="36" height="32" viewBox="0 0 36 32"><ellipse cx="19" cy="13" rx="14" ry="10" fill="none" stroke="#fff" stroke-width="2.4"/><path d="M9 20L4 29l11-6" fill="none" stroke="#fff" stroke-width="2.4"/></svg></div>
      <h3>Speaking</h3>
      <p>Lorem ipsum dolor sit amet, consectetur adipiscing elit. Maecenas feentum.</p>
      <span class="more">More info</span>
      <div class="pay">coinvy</div>
    </article>
    <article class="card">
      <div class="icon"><svg width="34" height="32" viewBox="0 0 34 32"><path d="M5 20v-5a12 12 0 0 1 24 0v5" fill="none" stroke="#fff" stroke-width="2.4"/><rect x="3" y="18" width="7" height="11" rx="2" fill="#fff"/><rect x="24" y="18" width="7" height="11" rx="2" fill="#fff"/></svg></div>
      <h3>Listening</h3>
      <p>Lorem ipsum dolor sit amet, consectetur adipiscing elit. Maecenas feentum.</p>
      <span class="more">More info</span>
      <div class="pay">coinvy</div>
    </article>
    <article class="card">
      <div class="icon"><svg width="34" height="32" viewBox="0 0 34 32"><rect x="3" y="6" width="22" height="23" fill="none" stroke="#fff" stroke-width="2"/><path d="M14 20L28 4l3 3-14 16-4 1z" fill="#fff"/></svg></div>
      <h3>Writing</h3>
      <p>Lorem ipsum dolor sit amet, consectetur adipiscing elit. Maecenas feentum.</p>
      <span class="more">More info</span>
      <div class="pay">coinvy</div>
    </article>
  </div>

  <section class="media">
    <h2 class="abs" style="left:148px;top:1738px">Pictures Gallery</h2>
    <h2 class="abs" style="left:628px;top:1738px">Our Video</h2>
    <div class="thumb abs" style="left:148px;top:1808px" role="img" aria-label="Photo of a student smiling"><div style="background:linear-gradient(#f1ece6,#d9c3a6)"></div></div>
    <div class="thumb abs" style="left:294px;top:1808px" role="img" aria-label="Photo of a student at a laptop"><div style="background:linear-gradient(#eeeeee,#c9c2bb)"></div></div>
    <div class="thumb abs" style="left:440px;top:1808px" role="img" aria-label="Photo of a student studying outdoors"><div style="background:linear-gradient(#b9c9a0,#6f8a5c)"></div></div>
    <div class="thumb abs" style="left:148px;top:1953px" role="img" aria-label="Photo of a student smiling"><div style="background:linear-gradient(#f1ece6,#d9c3a6)"></div></div>
    <div class="thumb abs" style="left:294px;top:1953px" role="img" aria-label="Photo of a student at a laptop"><div style="background:linear-gradient(#eeeeee,#c9c2bb)"></div></div>
    <div class="thumb abs" style="left:440px;top:1953px" role="img" aria-label="Photo of a student studying outdoors"><div style="background:linear-gradient(#b9c9a0,#6f8a5c)"></div></div>

    <div class="video abs" role="img" aria-label="Video still of a student using a laptop">
      <div class="video-play abs"><svg width="12" height="14" viewBox="0 0 12 14"><path d="M1 1l10 6-10 6z" fill="#fff"/></svg></div>
      <div class="video-tools abs"><b>LIKE</b><b>LATER</b><b>SHARE</b><b>EMBED</b></div>
      <div class="video-bar abs">
        <svg width="12" height="14" viewBox="0 0 12 14"><path d="M1 1l10 6-10 6z" fill="#fff"/></svg>
        <div class="track"><i></i></div>
        <span style="color:#fff;font-size:10px;font-weight:700">HD</span>
        <svg width="12" height="12" viewBox="0 0 12 12"><path d="M1 4V1h3M8 1h3v3M11 8v3H8M4 11H1V8" fill="none" stroke="#fff" stroke-width="1.5"/></svg>
      </div>
    </div>
  </section>

  <section class="steps abs"></section>
  <h2 class="section-title abs" style="top:2192px;left:0">How to Start QRAVE Tuition</h2>
  <div class="divider abs" style="left:440px"></div>
  <div class="divider abs" style="left:760px"></div>
  <div class="step abs" style="left:158px">
    <div class="step-icon"><svg width="84" height="74" viewBox="0 0 84 74"><rect x="10" y="4" width="64" height="52" rx="3" fill="none" stroke="#0292cd" stroke-width="5"/><rect x="0" y="60" width="84" height="8" rx="3" fill="#0292cd"/><path d="M30 24h7l9-8v28l-9-8h-7z" fill="#0292cd"/><path d="M51 22a9 9 0 0 1 0 16M55 17a15 15 0 0 1 0 26" fill="none" stroke="#0292cd" stroke-width="3"/></svg></div>
    <h3>Free Demo</h3>
    <p>Lorem ipsum dolor sit amet, consectetur adipiscing elit. Maecenas fermentum justo nec felis vestibulum.</p>
  </div>
  <div class="step abs" style="left:450px">
    <div class="step-icon"><svg width="80" height="80" viewBox="0 0 80 80"><circle cx="40" cy="40" r="38" fill="#0292cd"/></svg></div>
    <h3>Get Talvo</h3>
    <p>Lorem ipsum dolor sit amet, consectetur adipiscing elit. Maecenas fermentum justo nec felis vestibulum.</p>
  </div>
  <div class="step abs" style="left:768px">
    <div class="step-icon"><svg width="80" height="80" viewBox="0 0 80 80"><rect x="2" y="2" width="76" height="76" rx="8" fill="#0292cd"/></svg></div>
    <h3>Get Meshdesk</h3>
    <p>Lorem ipsum dolor sit amet, consectetur adipiscing elit. Maecenas fermentum justo nec felis vestibulum.</p>
  </div>

  <section class="newsletter abs">
    <h3>Subscribe Our Newsletter</h3>
    <div class="field">Enter Your Name</div>
    <div class="field">Enter Your Email Address</div>
    <div class="subscribe">Subscribe</div>
  </section>

  <footer class="site-footer abs">
    <div class="footer-links abs"><span>Tutorial Packages</span><span>Weekly Tips and Comments</span><span>Reading</span><span>Speaking</span><span>Listening</span><span>Writing</span></div>
    <div class="copyright abs">Copyright © 2014 www.lernmarowebtutor.example. All rights reserved.</div>
    <div class="footer-social abs"><b></b><b></b><b></b><b></b><b></b><b></b><b></b></div>
  </footer>

</div>
</body>
</html>
```